LuMarking-Tagvelory Partial Redesign - Web App

Are you able to apply your creativity to an existing layout? I’m convinced that even just a few touches can make a big difference to add personality and professionalism to a website design, and I’m looking for someone able to use existing ideas and bring them to the next level while keeping inside some given constraints.
The actual job is to improve an existing design concept and to apply it creatively to a landing page, a simple home page, and an older web app (single page website).
To help you start with a clear picture of the current situation and of my requirements, I created a detailed brief with screenshots, live examples, and complete instructions. You can find it attached to this job.
My tastes are inclined towards clean and simple designs. For this project I'm not looking for dazzling novelty, but for very solid craftsmanship. Are the right man - or woman - for the job?
Updates
I wanted to thank everybody who participated in this project. I made a choice, but also other designs were interesting. Hope to work with you another time.
Target Market(s)
Our main target is social media marketers and startuppers
Look and feel
Each slider illustrates characteristics of the customer's brand and the style your logo design should communicate.

```html
<!DOCTYPE html>
<html lang="en">
<head>
<meta charset="utf-8">
<title>LuMarking – Hashtag Explorer</title>
<link href="https://fonts.googleapis.com/css2?family=PT+Sans:wght@400;700&family=Arimo:wght@400;700&display=swap" rel="stylesheet">
<style>
  :root{
    --orange:#d9430f;
    --orange-line:#e0521f;
    --dark:#3b3e46;
    --dark-soft:#5b5e66;
    --band:#e1e1e3;
    --side:#efefef;
    --text:#3f3f3f;
    --muted:#6b6b6b;
    --card-border:#d8d8d8;
    --white:#ffffff;
  }
  *{box-sizing:border-box;margin:0;padding:0}
  html,body{width:1200px;height:900px;overflow:hidden;background:var(--white);font-family:"PT Sans",sans-serif;color:var(--text)}
  .page{position:relative;width:1200px;height:900px}
  .abs{position:absolute}

  .brand{left:150px;top:22px;display:flex;align-items:center;gap:14px}
  .brand-mark{width:44px;height:44px;background:var(--dark-soft);border-radius:50%}
  .brand-name{font-family:"Arimo",sans-serif;font-weight:700;font-size:38px;color:var(--dark-soft);letter-spacing:-1px}

  .social-count{top:53px;display:flex;align-items:center;gap:4px}
  .social-dot{width:30px;height:27px;border-radius:8px}
  .social-dot.tw{background:#4bb7ea}
  .social-dot.fb{background:#3b5a93}
  .social-num{background:#e4e4e4;padding:2px 8px;font-family:"Arimo",sans-serif;font-size:13px;color:#222;height:23px;line-height:19px}

  .nav{left:0;top:110px;width:1200px;height:34px;background:var(--dark)}
  .nav a{position:absolute;top:0;height:34px;line-height:34px;color:var(--white);font-weight:700;font-size:14px;text-decoration:none;text-align:center}
  .nav a.active{background:var(--orange)}

  .search-band{left:148px;top:144px;width:901px;height:70px;background:var(--band)}
  .search-box{left:160px;top:162px;width:276px;height:33px;background:var(--white);border:1px solid #d4d4d4;display:flex}
  .search-box span{flex:1;font-family:"Arimo",sans-serif;font-size:12px;line-height:31px;padding-left:11px;color:#333}
  .search-box i{width:33px;border-left:1px solid #d4d4d4;display:flex;align-items:center;justify-content:center}
  .found-label{left:591px;top:164px;font-size:14px;color:#444}
  .digits{left:750px;top:153px;display:flex;gap:0}
  .digit{width:26px;height:35px;margin-right:2px;background:#f6f6f6;border:1px solid #cfcfcf;font-family:"Arimo",sans-serif;font-size:22px;color:#888;text-align:center;line-height:33px}
  .tweets-total{left:921px;top:193px;font-size:11px;color:#555}

  .sidebar{left:745px;top:214px;width:304px;height:644px;background:var(--side);border-left:1px solid #e2e2e2}

  .tabs{left:150px;top:223px;width:573px;height:32px;background:var(--dark);border-radius:3px;display:flex}
  .tab{color:var(--white);font-size:11.5px;line-height:32px;text-align:center}
  .tab.active{background:var(--dark-soft);border-radius:3px 0 0 3px}
  .tab-pointer{left:219px;top:255px;width:0;height:0;border-left:7px solid transparent;border-right:7px solid transparent;border-top:9px solid var(--dark-soft)}

  .graph{left:0;top:0}
  .graph text{font-family:"PT Sans",sans-serif;font-size:13px;fill:var(--white);text-anchor:middle;dominant-baseline:middle}

  .mode{top:772px;height:26px;width:109px;color:var(--white);font-weight:700;font-size:13px;text-align:center;line-height:26px;border-radius:2px}
  .mode.advanced{left:521px;background:var(--dark)}
  .mode.simple{left:635px;background:var(--orange)}

  .side-title{left:758px;font-size:14px;color:#444}
  .feed{left:758px;width:276px;height:66px;background:var(--white);border:1px solid var(--card-border)}
  .avatar{position:absolute;left:9px;top:11px;width:49px;height:43px}
  .feed p{position:absolute;left:70px;top:8px;width:200px;font-family:"Arimo",sans-serif;font-size:11px;line-height:13px;color:#222}
  .feed .handle{color:#e06a1f;font-weight:700}
  .feed small{display:block;font-size:8.5px;margin-top:5px;color:#222}

  .influencers{left:760px;top:682px;list-style:none}
  .influencers li{height:22.5px;font-size:13px;color:#444;padding-left:26px;position:relative;line-height:22px}
  .influencers li::before{content:"";position:absolute;left:0;top:7px;border-left:7px solid #555;border-top:4px solid transparent;border-bottom:4px solid transparent}
  .tooltip{left:881px;top:680px;height:22px;padding:0 10px;background:var(--dark);color:var(--white);font-size:11.5px;line-height:22px}
  .tooltip::before{content:"";position:absolute;left:-6px;top:6px;border-right:6px solid var(--dark);border-top:5px solid transparent;border-bottom:5px solid transparent}

  .footer{left:0;top:858px;width:1200px;height:42px;background:var(--dark)}
  .footer .copy{position:absolute;left:150px;top:13px;font-size:11px;color:#bfc0c4}
  .footer .legal{position:absolute;left:957px;top:13px;font-size:11px;color:#bfc0c4}
  .footer .icons{position:absolute;left:570px;top:12px;display:flex;gap:4px}
  .footer .icons span{width:17px;height:17px;border-radius:2px}
</style>
</head>
<body>
<div class="page">

  <div class="abs brand"><div class="brand-mark"></div><span class="brand-name">LuMarking</span></div>

  <div class="abs social-count" style="left:778px"><div class="social-dot tw"></div><div class="social-num">336,365</div></div>
  <div class="abs social-count" style="left:909px"><div class="social-dot fb"></div><div class="social-num">336,365</div></div>

  <nav class="abs nav">
    <a class="active" style="left:151px;width:97px">About</a>
    <a style="left:266px;width:80px">Summary</a>
    <a style="left:379px;width:80px">Time line</a>
    <a style="left:497px;width:90px">Influencers</a>
    <a style="left:615px;width:80px">Hash tag</a>
    <a style="left:723px;width:60px">Blog</a>
  </nav>

  <div class="abs search-band"></div>
  <div class="abs search-box"><span>Search</span><i>
    <svg width="14" height="14" viewBox="0 0 14 14"><circle cx="5.5" cy="5.5" r="4" fill="none" stroke="#333" stroke-width="2"/><line x1="8.5" y1="8.5" x2="13" y2="13" stroke="#333" stroke-width="2.4"/></svg>
  </i></div>
  <div class="abs found-label">Hashtags found so far :</div>
  <div class="abs digits">
    <div class="digit">1</div><div class="digit">0</div><div class="digit">,</div><div class="digit">6</div><div class="digit">1</div><div class="digit">1</div><div class="digit">,</div><div class="digit">1</div><div class="digit">8</div><div class="digit">0</div>
  </div>
  <div class="abs tweets-total">in 567,419,411 tweets</div>

  <aside class="abs sidebar"></aside>

  <div class="abs tabs">
    <div class="tab active" style="width:166px">Top Related Hashtags | Free</div>
    <div class="tab" style="width:146px">Top Influencers Free</div>
    <div class="tab" style="width:110px">Variants &nbsp;Free</div>
    <div class="tab" style="width:151px">In-Depth Intelligence Pro</div>
  </div>
  <div class="abs tab-pointer"></div>

  <svg class="abs graph" width="745" height="800" viewBox="0 0 745 800">
    <g stroke="var(--orange-line)" stroke-width="1">
      <line x1="443" y1="503" x2="427" y2="342"/><line x1="443" y1="503" x2="576" y2="360"/>
      <line x1="443" y1="503" x2="299" y2="379"/><line x1="443" y1="503" x2="651" y2="458"/>
      <line x1="443" y1="503" x2="218" y2="494"/><line x1="443" y1="503" x2="671" y2="593"/>
      <line x1="443" y1="503" x2="553" y2="656"/><line x1="443" y1="503" x2="367" y2="623"/>
      <line x1="443" y1="503" x2="228" y2="640"/><line x1="443" y1="503" x2="415" y2="730"/>
    </g>
    <g fill="var(--orange)">
      <circle cx="443" cy="503" r="54"/><circle cx="427" cy="342" r="40"/><circle cx="576" cy="360" r="47"/>
      <circle cx="299" cy="379" r="47"/><circle cx="651" cy="458" r="47"/><circle cx="218" cy="501" r="45"/>
      <circle cx="671" cy="593" r="50"/><circle cx="553" cy="656" r="45"/><circle cx="367" cy="623" r="47"/>
      <circle cx="228" cy="640" r="54"/><circle cx="415" cy="730" r="48"/>
    </g>
    <text x="443" y="500">auto follow</text><text x="426" y="340">500 day</text><text x="576" y="359">100 day</text>
    <text x="301" y="380">follow me</text><text x="653" y="459">jim</text><text x="215" y="495">Back</text>
    <text x="674" y="594">instan follow</text><text x="553" y="656">instant follow</text><text x="371" y="621">follow</text>
    <text x="231" y="643">follow back</text><text x="419" y="728">back</text>
  </svg>

  <div class="abs mode advanced">ADVACE MODE</div>
  <div class="abs mode simple">SIMPLE MODE</div>

  <div class="abs side-title" style="top:235px">Latest Chirper Feeds :</div>

  <div class="abs feed" style="top:269px"><div class="avatar" role="img" aria-label="Profile photo of post author" style="background:linear-gradient(#cfc4b8,#8f8375)"></div><p><span class="handle">@Mirelon</span> laboris nisi ut aliquip ex ea s liamitcommodo cons liqui eq<small>46 mins ago - Reply - Repost - Favourite</small></p></div>
  <div class="abs feed" style="top:338px"><div class="avatar" role="img" aria-label="Profile photo of post author" style="background:linear-gradient(#e6e0d8,#7a6a5c)"></div><p><span class="handle">@Mirelon</span> laboris nisi ut aliquip ex ea s liamitcommodo cons liqui eq<small>46 mins ago - Reply - Repost - Favourite</small></p></div>
  <div class="abs feed" style="top:407px"><div class="avatar" role="img" aria-label="Profile photo of post author" style="background:linear-gradient(#7fa25a,#b58d6e)"></div><p><span class="handle">@Mirelon</span> laboris nisi ut aliquip ex ea s liamitcommodo cons liqui eq<small>46 mins ago - Reply - Repost - Favourite</small></p></div>
  <div class="abs feed" style="top:476px"><div class="avatar" role="img" aria-label="Profile photo of post author" style="background:linear-gradient(#5a4a3a,#c9a07e)"></div><p><span class="handle">@Mirelon</span> laboris nisi ut aliquip ex ea s liamitcommodo cons liqui eq<small>46 mins ago - Reply - Repost - Favourite</small></p></div>
  <div class="abs feed" style="top:545px"><div class="avatar" role="img" aria-label="Profile photo of post author" style="background:linear-gradient(#3b4a2a,#a07a5a)"></div><p><span class="handle">@Mirelon</span> laboris nisi ut aliquip ex ea s liamitcommodo cons liqui eq<small>46 mins ago - Reply - Repost - Favourite</small></p></div>

  <div class="abs side-title" style="top:646px">Hashtag Top Influencers</div>
  <ul class="abs influencers">
    <li>brightlanework</li><li>dalvenor</li><li>korrinhale</li><li>pelatrue_</li><li>quenvora</li>
  </ul>
  <div class="abs tooltip">Support 9684523 &nbsp;followers</div>

  <footer class="abs footer">
    <span class="copy">© 2012. LuMarking Ltd. All Rights Reserved.</span>
    <div class="icons"><span style="background:#3b5a93"></span><span style="background:#3fa9dd"></span><span style="background:#2a77b3"></span><span style="background:#555"></span><span style="background:#e8742a"></span></div>
    <span class="legal">Privacy Policy | T&amp;C</span>
  </footer>
</div>
</body>
</html>
```